Velmora Builders LLC- Bus. Cards, Door Hangers, Invoice, Estimates, Postcards
I want a proffessional package that express who we are and what we do. www.velmora-builders.example
Velmora Builders LLC- Bus. Cards, Door Hangers, Invoice, Estimates, Postcards - Construction
Creative Brief
Professional
Calvin Tressel
Owner
4216 Pellham Ave. Larkhaven, WL 80417
calvin@velmora-builders.example
www.velmora-builders.example
Spray Foam Insulation Energy Auditing Weatherization Thermal Imaging

```html
<!DOCTYPE html>
<html lang="en">
<head>
<meta charset="utf-8">
<title>Velmora Builders – Stationery Package</title>
<link href="https://fonts.googleapis.com/css2?family=Roboto:wght@400;500;700;900&display=swap" rel="stylesheet">
<style>
  :root{
    --green:#6db52b;
    --green-dark:#3f7f1c;
    --green-light:#a9d66a;
    --ink:#333;
    --muted:#8a8a8a;
    --rule:#cfcfcf;
    --paper:#ffffff;
    --sky-top:#2f7fd0;
    --sky-bottom:#cfe6f7;
    --bg-top:#c7e46a;
    --bg-mid:#4f9b2c;
    --bg-low:#1f4a55;
    --bg-bottom:#1b1b57;
  }
  *{box-sizing:border-box;margin:0;padding:0}
  html,body{width:1200px;height:670px;overflow:hidden}
  body{font-family:"Roboto",Arial,sans-serif;color:var(--ink)}
  .board{position:relative;width:1200px;height:670px;overflow:hidden;
    background:linear-gradient(180deg,var(--bg-top) 0%,var(--bg-mid) 30%,var(--bg-low) 58%,var(--bg-bottom) 100%)}
  .piece{position:absolute;background:var(--paper);box-shadow:0 3px 8px rgba(0,0,0,.25)}
  .label{position:absolute;font-size:7px;color:rgba(255,255,255,.85);letter-spacing:.2px;white-space:nowrap}

  .brand{display:flex;align-items:center;gap:4px;font-weight:700;color:var(--green);white-space:nowrap}
  .brand-mark{display:inline-block;background:var(--green)}
  .tagline{font-size:5px;color:var(--ink);white-space:nowrap}
  .tiny{font-size:4.5px;line-height:1.45;color:var(--ink);white-space:nowrap}

  /* envelope */
  .envelope-front{left:43px;top:43px;width:240px;height:96px}
  .envelope-front .brand{position:absolute;left:12px;top:10px;font-size:13px}
  .envelope-front .brand-mark{width:10px;height:10px}
  .envelope-front .tagline{position:absolute;left:12px;top:28px}
  .envelope-front .return-address{position:absolute;left:150px;top:11px}
  .envelope-front .window{position:absolute;left:24px;top:52px;width:78px;height:26px;background:#c8c8c8}
  .envelope-back{left:312px;top:43px;width:264px;height:96px}
  .envelope-back svg{position:absolute;inset:0}
  .envelope-back .flap-text{position:absolute;left:0;right:0;top:58px;text-align:center;font-size:4.5px;color:var(--muted)}

  /* business card */
  .business-card{left:679px;top:67px;width:173px;height:106px;border-radius:6px}
  .business-card .brand{position:absolute;left:10px;top:12px;font-size:11px}
  .business-card .brand-mark{width:9px;height:9px}
  .business-card .tagline{position:absolute;left:10px;top:27px;font-size:4.5px}
  .business-card .person{position:absolute;left:10px;top:44px;font-size:6px;font-weight:700}
  .business-card .person span{display:block;font-weight:400;font-size:5px;color:var(--muted)}
  .business-card .contact{position:absolute;left:90px;top:44px}
  .business-card .card-rule{position:absolute;left:0;right:0;bottom:12px;height:3px;background:var(--green)}

  /* forms */
  .form-sheet{top:211px;width:264px;height:370px}
  .invoice{left:43px}
  .estimate{left:324px}
  .form-sheet .brand{position:absolute;left:14px;top:16px;font-size:13px}
  .form-sheet .brand-mark{width:10px;height:10px}
  .form-sheet .tagline{position:absolute;left:14px;top:34px}
  .form-sheet .sender{position:absolute;left:168px;top:14px}
  .form-sheet .title-bar{position:absolute;left:14px;right:14px;top:58px;height:10px;background:#222;color:#fff;font-size:6px;font-weight:700;text-align:center;line-height:10px;letter-spacing:.5px}
  .form-sheet .title-bar::before{content:"";position:absolute;left:0;top:0;bottom:0;width:40%;background:var(--green)}
  .form-sheet .title-bar span{position:relative}
  .form-sheet .fields{position:absolute;left:14px;right:14px;top:76px;display:flex;justify-content:space-between}
  .form-sheet .field-line{width:100%;border-bottom:.5px solid var(--rule);font-size:4.5px;color:var(--muted);padding-bottom:2px;margin-bottom:4px}
  .form-sheet .field-col{width:48%}
  .form-sheet .field-col+.field-col{width:40%}
  .line-items{position:absolute;left:14px;right:14px;top:112px;width:236px;border-collapse:collapse;font-size:4.5px}
  .line-items th{background:#e6e6e6;text-align:left;padding:2px 3px;font-weight:500}
  .line-items td{border-bottom:.5px solid var(--rule);height:9px}
  .line-items td+td,.line-items th+th{border-left:.5px solid var(--rule)}
  .totals{position:absolute;right:14px;top:300px;width:80px;font-size:4.5px}
  .totals div{display:flex;justify-content:space-between;border-bottom:.5px solid var(--rule);padding:2px 0}
  .signature{position:absolute;left:14px;top:322px;width:110px;border-top:.5px solid var(--rule);font-size:4.5px;color:var(--muted);padding-top:2px}
  .form-footer{position:absolute;left:0;right:0;bottom:0;height:8px;background:var(--green)}

  /* postcard front */
  .postcard-front{left:619px;top:211px;width:317px;height:183px;overflow:hidden}
  .postcard-front .photo{position:absolute;inset:0;background:linear-gradient(180deg,var(--sky-top) 0%,var(--sky-bottom) 55%,#e8f2e0 100%)}
  .offer-tab{background:var(--green);color:#fff;font-weight:900;padding:0 10px}
  .postcard-front .offer-tab{position:absolute;left:0;top:14px;width:150px;height:18px;font-size:12px;line-height:18px}
  .service-list{list-style:none;font-weight:700;white-space:nowrap}
  .service-list li::before{content:"•";margin-right:5px}
  .postcard-front .service-list{position:absolute;left:12px;top:40px;color:#fff;font-size:14px;line-height:20px;text-shadow:0 1px 2px rgba(0,0,0,.35)}
  .discount{position:absolute;border-radius:50%;background:var(--green);color:#fff;text-align:center;font-weight:900;display:flex;flex-direction:column;justify-content:center;border:2px solid #fff}
  .discount small{font-size:.45em;font-weight:500}
  .postcard-front .discount{right:16px;top:52px;width:54px;height:54px;font-size:14px}
  .web-bar{position:absolute;background:var(--green);color:#fff;font-size:5px;text-align:center;white-space:nowrap}
  .postcard-front .web-bar{right:12px;bottom:12px;width:100px;height:9px;line-height:9px}

  /* postcard back */
  .postcard-back{left:619px;top:432px;width:317px;height:192px}
  .postcard-back .brand{position:absolute;left:14px;top:14px;font-size:13px}
  .postcard-back .brand-mark{width:10px;height:10px}
  .postcard-back .tagline{position:absolute;left:14px;top:32px}
  .postcard-back .return-address{position:absolute;left:14px;top:44px}
  .postcard-back .divider{position:absolute;left:166px;top:56px;height:100px;border-left:.6px solid var(--rule)}
  .postcard-back .stamp{position:absolute;right:14px;top:14px;width:30px;height:36px;border:.6px dashed var(--muted)}
  .postcard-back .address-lines{position:absolute;left:180px;top:90px;width:120px}
  .postcard-back .address-lines div{border-bottom:.6px solid var(--rule);height:14px}
  .postcard-back .service-strip{position:absolute;left:14px;right:14px;bottom:12px;font-size:6px;color:var(--green);letter-spacing:.3px;white-space:nowrap}

  /* door hanger */
  .door-hanger{left:1008px;top:43px;width:168px;height:586px;background:none;box-shadow:none;filter:drop-shadow(0 3px 6px rgba(0,0,0,.3))}
  .door-hanger .sheet{position:absolute;inset:0;background:var(--paper);clip-path:polygon(50% 0,100% 14%,100% 100%,0 100%,0 14%)}
  .door-hanger .hole{position:absolute;left:56px;top:48px;width:56px;height:56px;border-radius:50%;background:var(--bg-mid)}
  .door-hanger .brand{position:absolute;left:12px;top:118px;font-size:12px}
  .door-hanger .brand-mark{width:9px;height:9px}
  .door-hanger .tagline{position:absolute;left:12px;top:135px;font-size:4.5px}
  .door-hanger .photo{position:absolute;left:0;right:0;top:152px;height:120px;background:linear-gradient(180deg,var(--sky-top),var(--sky-bottom) 70%,#e3efd8)}
  .door-hanger .offer-tab{position:absolute;left:0;top:282px;width:120px;height:16px;font-size:11px;line-height:16px}
  .door-hanger .service-list{position:absolute;left:12px;top:306px;color:var(--ink);font-size:11.5px;line-height:19px}
  .door-hanger .discount{right:14px;top:392px;width:50px;height:50px;font-size:13px}
  .door-hanger .web-bar{left:12px;right:12px;top:470px;height:10px;line-height:10px}
  .door-hanger .fine-print{position:absolute;left:12px;right:12px;top:492px;font-size:4.5px;color:var(--muted);line-height:1.5}

  /* email signature */
  .email-signature{left:132px;top:600px;width:348px;height:53px}
  .email-signature .person{position:absolute;left:10px;top:7px;font-size:6px;font-weight:700}
  .email-signature .person span{display:block;font-weight:400;font-size:5px;color:var(--muted)}
  .email-signature .brand{position:absolute;left:110px;top:8px;font-size:11px}
  .email-signature .brand-mark{width:9px;height:9px}
  .email-signature .contact-line{position:absolute;left:10px;right:10px;bottom:6px;font-size:4.5px;color:var(--muted);border-top:.6px solid var(--green);padding-top:3px;white-space:nowrap}
</style>
</head>
<body>
<main class="board">

  <span class="label" style="left:120px;top:30px">Envelope Front</span>
  <section class="piece envelope-front">
    <div class="brand"><i class="brand-mark"></i>Velmora Builders</div>
    <p class="tagline">Sealing Comfort Into Every Room We Touch</p>
    <p class="tiny return-address">4216 Pellham Ave.<br>Larkhaven, WL 80417</p>
    <div class="window"></div>
  </section>

  <span class="label" style="left:405px;top:30px">Envelope Back</span>
  <section class="piece envelope-back">
    <svg width="264" height="96" viewBox="0 0 264 96" aria-hidden="true">
      <polyline points="0,0 132,52 264,0" fill="none" stroke="#d4d4d4" stroke-width=".8"/>
      <polyline points="0,96 110,46" fill="none" stroke="#e4e4e4" stroke-width=".8"/>
      <polyline points="264,96 154,46" fill="none" stroke="#e4e4e4" stroke-width=".8"/>
    </svg>
    <p class="flap-text">Velmora Builders · 4216 Pellham Ave. · Larkhaven, WL 80417</p>
  </section>

  <section class="piece business-card">
    <div class="brand"><i class="brand-mark"></i>Velmora Builders</div>
    <p class="tagline">Sealing Comfort Into Every Room We Touch</p>
    <p class="person">Calvin Tressel<span>Owner</span></p>
    <p class="tiny contact">4216 Pellham Ave.<br>Larkhaven, WL 80417<br>P (303) 555-0142<br>F (303) 555-0143<br>calvin@velmora-builders.example<br>www.velmora-builders.example</p>
    <div class="card-rule"></div>
  </section>
  <span class="label" style="left:735px;top:180px">Business card FRONT</span>

  <section class="piece form-sheet invoice">
    <div class="brand"><i class="brand-mark"></i>Velmora Builders</div>
    <p class="tagline">Sealing Comfort Into Every Room We Touch</p>
    <p class="tiny sender">4216 Pellham Ave.<br>Larkhaven, WL 80417<br>P (303) 555-0142<br>F (303) 555-0143</p>
    <div class="title-bar"><span>INVOICE</span></div>
    <div class="fields">
      <div class="field-col"><p class="field-line">Bill To:</p><p class="field-line">Address:</p><p class="field-line">Phone:</p></div>
      <div class="field-col"><p class="field-line">Invoice No:</p><p class="field-line">Date:</p><p class="field-line">Terms:</p></div>
    </div>
    <table class="line-items">
      <thead><tr><th style="width:14%">Qty</th><th>Description</th><th style="width:18%">Rate</th><th style="width:18%">Amount</th></tr></thead>
      <tbody>
        <tr><td></td><td></td><td></td><td></td></tr><tr><td></td><td></td><td></td><td></td></tr>
        <tr><td></td><td></td><td></td><td></td></tr><tr><td></td><td></td><td></td><td></td></tr>
        <tr><td></td><td></td><td></td><td></td></tr><tr><td></td><td></td><td></td><td></td></tr>
        <tr><td></td><td></td><td></td><td></td></tr><tr><td></td><td></td><td></td><td></td></tr>
        <tr><td></td><td></td><td></td><td></td></tr><tr><td></td><td></td><td></td><td></td></tr>
        <tr><td></td><td></td><td></td><td></td></tr><tr><td></td><td></td><td></td><td></td></tr>
        <tr><td></td><td></td><td></td><td></td></tr><tr><td></td><td></td><td></td><td></td></tr>
        <tr><td></td><td></td><td></td><td></td></tr><tr><td></td><td></td><td></td><td></td></tr>
        <tr><td></td><td></td><td></td><td></td></tr>
      </tbody>
    </table>
    <div class="totals"><div><span>Subtotal</span><span></span></div><div><span>Tax</span><span></span></div><div><strong>Total</strong><span></span></div></div>
    <p class="signature">Authorized Signature</p>
    <div class="form-footer"></div>
  </section>
  <span class="label" style="left:160px;top:585px">Invoice</span>

  <section class="piece form-sheet estimate">
    <div class="brand"><i class="brand-mark"></i>Velmora Builders</div>
    <p class="tagline">Sealing Comfort Into Every Room We Touch</p>
    <p class="tiny sender">4216 Pellham Ave.<br>Larkhaven, WL 80417<br>P (303) 555-0142<br>F (303) 555-0143</p>
    <div class="title-bar"><span>ESTIMATE</span></div>
    <div class="fields">
      <div class="field-col"><p class="field-line">Customer:</p><p class="field-line">Address:</p><p class="field-line">Phone:</p></div>
      <div class="field-col"><p class="field-line">Estimate No:</p><p class="field-line">Date:</p><p class="field-line">Valid Until:</p></div>
    </div>
    <table class="line-items">
      <thead><tr><th style="width:14%">Qty</th><th>Description</th><th style="width:18%">Rate</th><th style="width:18%">Amount</th></tr></thead>
      <tbody>
        <tr><td></td><td></td><td></td><td></td></tr><tr><td></td><td></td><td></td><td></td></tr>
        <tr><td></td><td></td><td></td><td></td></tr><tr><td></td><td></td><td></td><td></td></tr>
        <tr><td></td><td></td><td></td><td></td></tr><tr><td></td><td></td><td></td><td></td></tr>
        <tr><td></td><td></td><td></td><td></td></tr><tr><td></td><td></td><td></td><td></td></tr>
        <tr><td></td><td></td><td></td><td></td></tr><tr><td></td><td></td><td></td><td></td></tr>
        <tr><td></td><td></td><td></td><td></td></tr><tr><td></td><td></td><td></td><td></td></tr>
        <tr><td></td><td></td><td></td><td></td></tr><tr><td></td><td></td><td></td><td></td></tr>
        <tr><td></td><td></td><td></td><td></td></tr><tr><td></td><td></td><td></td><td></td></tr>
        <tr><td></td><td></td><td></td><td></td></tr>
      </tbody>
    </table>
    <div class="totals"><div><span>Subtotal</span><span></span></div><div><span>Tax</span><span></span></div><div><strong>Total</strong><span></span></div></div>
    <p class="signature">Customer Approval</p>
    <div class="form-footer"></div>
  </section>
  <span class="label" style="left:440px;top:585px">Estimate</span>

  <section class="piece postcard-front">
    <div class="photo" role="img" aria-label="Photo of an energy-efficient home under a bright blue sky"></div>
    <p class="offer-tab">We offer:</p>
    <ul class="service-list">
      <li>Spray Foam Insulation</li>
      <li>Energy Auditing</li>
      <li>Weatherization</li>
      <li>Thermal Imaging</li>
    </ul>
    <p class="discount">10%<small>OFF</small></p>
    <p class="web-bar">www.velmora-builders.example</p>
  </section>
  <span class="label" style="left:755px;top:400px">Postcard Front</span>

  <section class="piece postcard-back">
    <div class="brand"><i class="brand-mark"></i>Velmora Builders</div>
    <p class="tagline">Sealing Comfort Into Every Room We Touch</p>
    <p class="tiny return-address">4216 Pellham Ave. · Larkhaven, WL 80417</p>
    <div class="divider"></div>
    <div class="stamp"></div>
    <div class="address-lines"><div></div><div></div><div></div></div>
    <p class="service-strip">Spray Foam Insulation · Energy Auditing · Weatherization · Thermal Imaging</p>
  </section>
  <span class="label" style="left:755px;top:628px">Postcard Back</span>

  <section class="piece door-hanger">
    <div class="sheet"></div>
    <div class="hole"></div>
    <div class="brand"><i class="brand-mark"></i>Velmora Builders</div>
    <p class="tagline">Sealing Comfort Into Every Room We Touch</p>
    <div class="photo" role="img" aria-label="Photo of a home exterior against a blue sky"></div>
    <p class="offer-tab">We offer:</p>
    <ul class="service-list">
      <li>Spray Foam Insulation</li>
      <li>Energy Auditing</li>
      <li>Weatherization</li>
      <li>Thermal Imaging</li>
    </ul>
    <p class="discount">10%<small>OFF</small></p>
    <p class="web-bar">www.velmora-builders.example</p>
    <p class="fine-print">Call today for a free home energy review. (303) 555-0142 · Offer valid on new projects only.</p>
  </section>
  <span class="label" style="left:1072px;top:634px">Door Hanger</span>

  <section class="piece email-signature">
    <p class="person">Calvin Tressel<span>Owner</span></p>
    <div class="brand"><i class="brand-mark"></i>Velmora Builders</div>
    <p class="contact-line">4216 Pellham Ave. Larkhaven, WL 80417 · P (303) 555-0142 · calvin@velmora-builders.example · www.velmora-builders.example</p>
  </section>
  <span class="label" style="left:488px;top:622px">E-mail Signature</span>

</main>
</body>
</html>
```